International Dating Site for modern people

We need a site design for a brand new dating site. Feel free to express your ideas and creativity. The final design should be creative and positive feeling, warm.

major elements:
- main page
- login/logout (form)
- profile editing (form)
- profile page with pictures
- search page and results page (form, table)
- a message box or the header in the main page with the following theme, feeling:
winter, spring, summer, autumn, christmas, easter, new year
- blog subpage (title, content)
- menu (login/blog/search/profile/logout)
- footer (impressum, faq, contact, privacy policy)

Target Market(s)

people between 21 and 45

Industry/Entity Type

Social

Number of Pages Required

4 page

Font styles to use
Sans Serif

Requirements
Must have
• happy, positive, warm look and feel and responsive design (plan to target different devices, the final and coded version will be responsive but please think of it when you design elements)
Nice to have
• creative

```html
<!DOCTYPE html>
<html lang="en">
<head>
<meta charset="utf-8">
<title>Warm Hearts — International Dating</title>
<link rel="stylesheet" href="https://fonts.googleapis.com/css2?family=Dancing+Script:wght@600;700&family=Jost:wght@400;500;600&display=swap">
<style>
:root{
  --pink:#e2587a;
  --pink-dark:#c9415f;
  --gold:#e9a83a;
  --sand:#ecc27a;
  --light:#ececec;
  --ink:#2a2a2a;
  --text:#555;
  --white:#fff;
  --black:#0d0d0d;
  --script:'Dancing Script', cursive;
  --sans:'Jost', sans-serif;
}
*{box-sizing:border-box;margin:0;padding:0}
html,body{width:1200px;height:2894px;overflow:hidden}
body{position:relative;font-family:var(--sans);color:var(--text);background:var(--light)}
.abs{position:absolute}
section,header,footer{position:absolute;left:0;width:1200px}

/* hero */
.hero{top:0;height:579px;background:linear-gradient(180deg,#6d5a45 0%,#9a7a52 45%,#b07a3e 75%,#5a3e28 100%)}
.brand{left:164px;top:28px;display:flex;align-items:center;gap:10px;color:var(--white);font-family:var(--sans);font-weight:600;font-size:28px;letter-spacing:.5px}
.brand-dot{width:34px;height:34px;border-radius:50%;background:var(--pink)}
.nav{left:500px;top:40px;display:flex}
.nav a{color:var(--white);text-decoration:none;font-size:13px;width:70px;text-align:center}
.btn-login,.btn-logout{top:33px;height:33px;width:79px;font-size:12px;color:var(--white);display:flex;align-items:center;justify-content:center;letter-spacing:.5px}
.btn-login{left:868px;background:var(--black);border:1px solid #777;outline:1px solid #000}
.btn-logout{left:957px;background:var(--pink);border:1px solid #f39ab0}
.slider{left:164px;top:89px;width:878px;height:374px;border:8px solid var(--white);background:linear-gradient(135deg,#c99a52 0%,#8a6a3c 40%,#4b5a4a 70%,#2f3a44 100%)}
.slider-title{left:60px;top:140px;font-family:var(--script);font-weight:700;font-size:42px;line-height:50px;color:var(--white);text-shadow:1px 2px 4px rgba(0,0,0,.5)}
.arrow{width:26px;height:38px;background:rgba(0,0,0,.55);display:flex;align-items:center;justify-content:center}
.signup{left:164px;top:482px;width:874px;height:81px;background:rgba(20,15,10,.6)}
.signup h4{position:absolute;left:10px;top:12px;color:var(--white);font-size:13px;font-weight:500;letter-spacing:.5px}
.select{top:37px;height:29px;background:var(--white);font-size:10px;color:#666;padding:0 8px;display:flex;align-items:center;justify-content:space-between}
.select::after{content:"";width:5px;height:5px;border-right:1px solid #888;border-bottom:1px solid #888;transform:rotate(45deg)}
.btn-next{left:750px;top:37px;width:108px;height:29px;background:var(--gold);color:var(--ink);font-size:11px;font-weight:600;display:flex;align-items:center;justify-content:center}

/* headings */
.heading{left:0;width:1200px;text-align:center;font-family:var(--script);font-weight:700;font-size:30px;color:var(--ink)}
.heading em{font-style:normal;color:var(--pink)}
.heading.light{color:var(--white)}
.heading-rule{left:540px;width:120px;height:2px;background:var(--pink)}
.heading-rule::after{content:"";position:absolute;left:54px;top:-4px;width:10px;height:10px;background:inherit;transform:rotate(45deg)}
.heading-rule.light{background:var(--white)}

/* about */
.about{top:579px;height:331px;background:var(--light)}
.about-dots{left:0;top:120px;width:190px;height:170px;background:radial-gradient(circle,#d8d8d8 35%,transparent 70%);opacity:.7}
.about-photo{width:100px;height:100px;border-radius:50%;border:3px solid var(--pink);background:linear-gradient(135deg,#d9b8a0,#9a6c58);box-shadow:0 12px 10px -8px rgba(0,0,0,.25)}
.about-photo.gold{border-color:var(--gold);background:linear-gradient(135deg,#c9d4dc,#8f7a66)}
.about-text{left:579px;top:150px;width:464px;font-size:11.5px;line-height:20px;color:var(--text)}

/* profiles */
.profiles{top:910px;height:434px;background:linear-gradient(180deg,#efc57f,#e9bb6d);}
.profiles-bg{left:300px;top:0;width:600px;height:434px;background:radial-gradient(ellipse at center,rgba(120,80,50,.25),transparent 70%)}
.card{top:141px;width:203px;height:224px;overflow:hidden}
.card-photo{position:absolute;inset:0;background:linear-gradient(160deg,#7b5a48,#2e2420)}
.card-name{position:absolute;left:0;bottom:0;width:100%;height:38px;background:rgba(10,10,10,.85);color:var(--white);font-size:15px;padding:10px 16px}
.age{position:absolute;right:4px;bottom:2px;width:50px;height:50px;border-radius:50%;background:var(--pink);color:var(--white);text-align:center;font-size:16px;line-height:16px;padding-top:8px}
.age small{display:block;font-size:8px;line-height:9px}
.p-arrow{top:233px;width:22px;height:38px;background:rgba(60,50,40,.6);display:flex;align-items:center;justify-content:center}

/* steps */
.steps{top:1344px;height:365px;background:var(--light)}
.step{top:160px;width:240px;text-align:center}
.step svg{display:block;margin:0 auto 14px}
.step h5{font-size:15.5px;font-weight:500;color:var(--ink)}
.step p{font-size:11px;line-height:14px;color:var(--text);margin-top:4px}

/* blog */
.blog{top:1709px;height:490px;background:linear-gradient(180deg,#e9c1bf 0%,#efd3c9 40%,#e7b79c 70%,#6c7a3a 92%,#4f5a2a 100%)}
.blog-photo{top:139px;width:201px;height:226px;background:linear-gradient(150deg,#c9a27a,#6e7f8e)}
.blog-text{top:154px;width:225px;height:201px;background:var(--white);padding:26px 14px 0 14px;box-shadow:2px 4px 10px rgba(0,0,0,.15)}
.blog-text h6{font-size:12.5px;line-height:15px;font-weight:500;color:var(--pink)}
.blog-text p{font-size:10.5px;line-height:13.5px;color:var(--text);margin-top:10px}
.blog-text a{display:inline-block;margin-top:10px;font-size:10.5px;color:var(--ink);text-decoration:underline;font-weight:600}
.date{top:165px;width:45px;height:48px;background:var(--white);text-align:center;font-size:20px;color:var(--ink);padding-top:2px}
.date span{display:block;margin-top:2px;background:var(--gold);color:var(--white);font-size:13px;height:20px;line-height:20px}
.blog-scene{left:870px;top:80px;width:330px;height:400px;background:radial-gradient(ellipse at 55% 45%,rgba(240,220,200,.7),transparent 70%)}
.dots{left:576px;top:415px;display:flex;gap:6px}
.dots i{width:8px;height:8px;border-radius:50%;background:var(--pink-dark)}
.dots i:first-child{background:#999}

/* subscribe */
.subscribe{top:2199px;height:305px;background:var(--light)}
.sub-art{left:199px;top:48px;width:290px;height:257px;background:radial-gradient(ellipse at 50% 40%,#f5b9c8 0%,#f7d6de 55%,transparent 72%)}
.sub-title{left:554px;top:103px;font-family:var(--script);font-weight:700;font-size:26px;color:var(--ink)}
.sub-title em{font-style:normal;color:var(--pink)}
.sub-rule{left:554px;top:146px;width:60px;height:2px;background:var(--pink)}
.sub-note{left:554px;top:170px;font-size:12px;line-height:15px;color:var(--ink)}
.sub-input{left:554px;top:216px;width:308px;height:27px;background:var(--white);border:1px solid #ccc}
.sub-btn{left:862px;top:216px;width:83px;height:27px;background:var(--pink);color:var(--white);font-size:12px;display:flex;align-items:center;justify-content:center}

/* footer */
.footer{top:2504px;height:312px;background:radial-gradient(circle,#1a1a1a 1px,transparent 2px) 0 0/14px 14px,var(--black)}
.footer .brand{left:0;width:1200px;top:68px;justify-content:center}
.f-line{left:0;width:1200px;text-align:center;color:var(--white)}
.f-address{top:162px;font-size:15px}
.f-phone{top:196px;font-size:30px;display:flex;justify-content:center;align-items:center;gap:8px}
.f-mail{top:252px;font-size:15px}
.bottom{top:2816px;height:78px;background:#f1f1f1}
.bottom-links{left:328px;top:12px;width:540px;display:flex;justify-content:space-between;font-size:12px;color:var(--ink);border-bottom:1px solid #ccc;padding-bottom:8px}
.bottom-links span{color:#999}
.copy{left:0;width:1200px;top:50px;text-align:center;font-size:11.5px;color:var(--ink)}
</style>
</head>
<body>

<header class="hero" role="img" aria-label="Autumn lakeside scene in warm browns behind the header">
  <div class="abs brand"><span class="brand-dot"></span>Warm Hearts</div>
  <nav class="abs nav"><a>Home</a><a>Profile</a><a>Search</a><a>Blog</a><a>Contact</a></nav>
  <div class="abs btn-login">LOGIN</div>
  <div class="abs btn-logout">LOGOUT</div>

  <div class="abs arrow" style="left:136px;top:257px"><svg width="10" height="16" viewBox="0 0 10 16"><path d="M8 1 2 8l6 7" fill="none" stroke="#fff" stroke-width="2"/></svg></div>
  <div class="abs arrow" style="left:1041px;top:257px"><svg width="10" height="16" viewBox="0 0 10 16"><path d="m2 1 6 7-6 7" fill="none" stroke="#fff" stroke-width="2"/></svg></div>

  <div class="abs slider" role="img" aria-label="Photo of a couple embracing by an autumn lake">
    <div class="abs slider-title">It All Starts With<br>A Little Faith...</div>
  </div>

  <form class="abs signup">
    <h4>CREATE YOUR FREE PROFILE</h4>
    <div class="abs select" style="left:10px;width:167px">I am</div>
    <div class="abs select" style="left:191px;width:168px">and Wanted</div>
    <div class="abs select" style="left:372px;width:176px">between</div>
    <div class="abs select" style="left:561px;width:176px">living in</div>
    <div class="abs btn-next">NEXT</div>
  </form>
</header>

<section class="about">
  <div class="abs about-dots" role="img" aria-label="Faint mosaic of member photos"></div>
  <h2 class="abs heading" style="top:56px">About <em>Warm Hearts</em></h2>
  <div class="abs heading-rule" style="top:102px"></div>
  <div class="abs about-photo" role="img" aria-label="Photo of a smiling couple" style="left:182px;top:148px"></div>
  <div class="abs about-photo gold" role="img" aria-label="Photo of a happy couple" style="left:309px;top:148px"></div>
  <div class="abs about-photo" role="img" aria-label="Photo of a couple with roses" style="left:436px;top:148px"></div>
  <p class="abs about-text">Ut wisi enim ad minim veniam, quis nostrud exerci tation ullamcorpk susci lobortis nisls ut aliquip ex ea commodo consequat. Duis autl vel eum iriure dolor in hendr vulputatel velit esse molestie conl quat, vel illum dolore eu feugiat nulla facilisiss a vero eros ektt accumnet iusto odio dignissim qui blandit praesent luptat delenitml augl dui dolorelw te feugait qui blandit nullaillum dolore facilisi.</p>
</section>

<section class="profiles">
  <div class="abs profiles-bg" role="img" aria-label="Soft background photo of a couple"></div>
  <h2 class="abs heading light" style="top:50px">Latest Profile</h2>
  <div class="abs heading-rule light" style="left:540px;top:96px"></div>

  <div class="abs p-arrow" style="left:136px"><svg width="8" height="14" viewBox="0 0 8 14"><path d="M7 1 1 7l6 6" fill="none" stroke="#fff" stroke-width="2"/></svg></div>
  <div class="abs p-arrow" style="left:1042px"><svg width="8" height="14" viewBox="0 0 8 14"><path d="m1 1 6 6-6 6" fill="none" stroke="#fff" stroke-width="2"/></svg></div>

  <div class="abs card" style="left:162px"><div class="card-photo" role="img" aria-label="Portrait photo of Becky"></div><div class="card-name">Becky</div><div class="age">22<small>Years<br>old</small></div></div>
  <div class="abs card" style="left:386px"><div class="card-photo" role="img" aria-label="Portrait photo of Piter"></div><div class="card-name">Piter</div><div class="age">28<small>Years<br>old</small></div></div>
  <div class="abs card" style="left:611px"><div class="card-photo" role="img" aria-label="Portrait photo of Carla"></div><div class="card-name">Carla</div><div class="age">26<small>Years<br>old</small></div></div>
  <div class="abs card" style="left:835px"><div class="card-photo" role="img" aria-label="Black and white portrait photo of Jack" style="background:linear-gradient(160deg,#9a9a9a,#2a2a2a)"></div><div class="card-name">Jack</div><div class="age">30<small>Years<br>old</small></div></div>
</section>

<section class="steps">
  <h2 class="abs heading" style="top:70px">How <em>It Work</em></h2>
  <div class="abs heading-rule" style="top:116px"></div>

  <div class="abs step" style="left:137px">
    <svg width="64" height="56" viewBox="0 0 64 56"><rect x="6" y="8" width="44" height="44" rx="8" fill="none" stroke="var(--pink)" stroke-width="5"/><path d="M24 38l3-10 24-24 8 8-24 24z" fill="var(--pink)" stroke="var(--light)" stroke-width="2"/></svg>
    <h5>Register On Our Website</h5><p>Duis autl ve iriure dolor hendrerit<br>in vulputate velit esse.</p>
  </div>
  <div class="abs step" style="left:372px">
    <svg width="76" height="56" viewBox="0 0 76 56"><rect x="12" y="4" width="52" height="38" rx="3" fill="var(--gold)"/><rect x="17" y="9" width="42" height="28" fill="var(--light)"/><circle cx="38" cy="19" r="5" fill="var(--gold)"/><path d="M29 33a9 7 0 0 1 18 0z" fill="var(--gold)"/><path d="M2 46h72l-5 6H7z" fill="var(--gold)"/></svg>
    <h5>Add Information About Yourself</h5><p>Duis autl ve iriure dolor hendrerit<br>in vulputate velit esse.</p>
  </div>
  <div class="abs step" style="left:623px">
    <svg width="64" height="56" viewBox="0 0 64 56"><circle cx="32" cy="12" r="9" fill="var(--pink)"/><circle cx="14" cy="28" r="8" fill="var(--pink)"/><circle cx="50" cy="28" r="8" fill="var(--pink)"/><path d="M20 34a12 10 0 0 1 24 0v4H20z" fill="var(--pink)"/><path d="M2 52a12 11 0 0 1 24 0zM38 52a12 11 0 0 1 24 0z" fill="var(--pink)"/></svg>
    <h5>Analyze The List Of People</h5><p>Duis autl ve iriure dolor hendrerit<br>in vulputate velit esse.</p>
  </div>
  <div class="abs step" style="left:839px">
    <svg width="60" height="56" viewBox="0 0 60 56"><path d="M30 52 6 28C-2 18 4 4 16 4c6 0 11 4 14 9 3-5 8-9 14-9 12 0 18 14 10 24z" fill="var(--gold)"/></svg>
    <h5>Find Your LOVE</h5><p>Duis autl ve iriure dolor hendrerit<br>in vulputate velit esse.</p>
  </div>
</section>

<section class="blog" role="img" aria-label="Sunset meadow picnic scene with a couple">
  <div class="abs blog-scene" role="img" aria-label="Photo of a woman relaxing at a picnic"></div>
  <h2 class="abs heading" style="top:58px">Latest <em>Blog</em></h2>
  <div class="abs heading-rule" style="top:104px"></div>

  <div class="abs blog-photo" role="img" aria-label="Photo of a laughing couple eating ice cream" style="left:162px"></div>
  <div class="abs blog-text" style="left:363px"><h6>Ut wisi enim ad minim veniam,<br>qunostodo consequat.</h6><p>Duis autl vel eum iriure dolor in lk hendr vulputatel velit es molestie conl quat, vel illum dol dignissim qui blandit praesen lup delenitml lanre facilisi.</p><a>Read More »</a></div>
  <div class="abs date" style="left:318px">21<span>Oct</span></div>

  <div class="abs blog-photo" role="img" aria-label="Photo of a couple sitting on a pier" style="left:611px;background:linear-gradient(160deg,#e8c9b0,#8f8a7a)"></div>
  <div class="abs blog-text" style="left:814px"><h6>Ut wisi enim ad minim veniam,<br>qunostodo consequat.</h6><p>Duis autl vel eum iriure dolor in lk hendr vulputatel velit es molestie conl quat, vel illum dol dignissim qui blandit praesen lup delenitml lanre facilisi.</p><a>Read More »</a></div>
  <div class="abs date" style="left:769px">21<span>Oct</span></div>

  <div class="abs dots"><i></i><i></i><i></i></div>
</section>

<section class="subscribe">
  <div class="abs sub-art" role="img" aria-label="Illustration of a couple at a café table under a floral heart"></div>
  <h2 class="abs sub-title">Subscribe For <em>Latest News</em></h2>
  <div class="abs sub-rule"></div>
  <p class="abs sub-note">Get the latest updates by<br>entering your email address</p>
  <svg class="abs" style="left:866px;top:152px" width="60" height="48" viewBox="0 0 60 48"><path d="M2 20 58 2 40 46 30 28z" fill="#111"/><path d="M30 28 58 2" stroke="var(--light)" stroke-width="2"/></svg>
  <div class="abs sub-input"></div>
  <div class="abs sub-btn">Subscribe</div>
</section>

<footer class="footer">
  <div class="abs brand"><span class="brand-dot"></span>Warm Hearts</div>
  <p class="abs f-line f-address">118 Rosewood Lane, Brightfield Avenue BF-2210</p>
  <p class="abs f-line f-phone"><svg width="32" height="32" viewBox="0 0 32 32"><circle cx="16" cy="16" r="14" fill="none" stroke="#fff" stroke-width="2.5"/><path d="M11 9c-2 2-1 6 3 10s8 5 10 3l-3-3-2 1c-2-1-4-3-5-5l1-2z" fill="#fff"/></svg>555 014 2280</p>
  <p class="abs f-line f-mail">info@warmhearts.example</p>
</footer>

<div class="abs bottom" style="left:0;width:1200px">
  <div class="abs bottom-links"><span>|</span>IMPRESSUM<span>|</span>FAQ<span>|</span>CONTACT<span>|</span>PRIVACY POLICY<span>|</span></div>
  <p class="abs copy">Copyright © 2016 Warm Hearts. All Rights Reserved.</p>
</div>

</body>
</html>
```